Business Card Design

I require the design of business cards using my exisiting logo.

It is essential that the designer has experience with various print processes (foil stamping etc) and different paper stock.

The design is to blend in with current packaging and display unit. (Images will be provided).
A swing tag and certificate of authenticity design will als be required at a later stage.

Details which need to be included on the card are:
- Contact Name
- Position in Company
- Address
- Contact Number
- Email Address
- Web Address

Ideally I would prefer the background (both sides) to be greyish colour (offset printing or if you can suggest greyish paperstock) with silver foiling on the front and either black or metallic silver on the back.

Or another option would be grey background on the front and either white or black on the the back.

* The business card can be portrait or landscape.

Printers specifications:
Bleed 3mm
Trim Marks
Seperate file for foil printing

This task is for someone who is creative and enjoys working with fashion and luxury items!
_______________________________________________

I will require business cards designs for 2 different business and would hope to work with the same designer.

Please note I had asked for a grey colour at least on one of the sides. However I keep on getting black and white designs.   

Business

• - Double sided business card
- Luxury feel
- Foil Print Priniting

- Would prefer at least grey background at least on one side of the card.

- The business card can be portrait or landscape.
• *The business card can be portrait or landscape.
• - Bright Colours
- Alterations to logo

```html
<!DOCTYPE html>
<html lang="en">
<head>
<meta charset="utf-8">
<title>Ora Jewels – Business Card</title>
<link rel="stylesheet" href="https://fonts.googleapis.com/css2?family=Open+Sans:wght@300;400;700&display=swap">
<style>
  :root {
    --backdrop: #ece9e5;
    --card-grey-light: #f4f4f4;
    --card-grey: #dcdcdc;
    --card-white: #ffffff;
    --ink: #1e1e1e;
    --ink-soft: #555555;
    --border: #111111;
  }
  * { margin: 0; padding: 0; box-sizing: border-box; }
  html, body {
    width: 1200px;
    height: 849px;
    overflow: hidden;
    background: var(--backdrop);
    font-family: "Open Sans", Arial, sans-serif;
  }
  .canvas { position: relative; width: 1200px; height: 849px; }

  .card {
    position: absolute;
    width: 402px;
    height: 704px;
    border-radius: 22px;
    text-align: center;
  }
  .card-front {
    left: 114px;
    top: 60px;
    background: radial-gradient(ellipse at 50% 40%, var(--card-grey-light) 0%, #ebebeb 55%, var(--card-grey) 100%);
  }
  .card-back {
    left: 638px;
    top: 65px;
    background: var(--card-white);
    border: 2px solid var(--border);
  }

  .holder {
    position: absolute;
    top: 38px;
    width: 100%;
    font-size: 26px;
    color: var(--ink-soft);
  }
  .holder-name { font-weight: 700; }
  .holder-position { font-size: 21px; font-weight: 400; }

  .brand-mark {
    position: absolute;
    left: 50%;
    border: 3px solid var(--ink);
    border-radius: 50%;
    transform: translateX(-50%);
  }
  .card-front .brand-mark { top: 200px; width: 100px; height: 100px; }
  .card-back .brand-mark { top: 205px; width: 110px; height: 110px; }

  .brand-name {
    position: absolute;
    width: 100%;
    font-weight: 300;
    color: var(--ink);
    letter-spacing: 1px;
  }
  .card-front .brand-name { top: 385px; font-size: 52px; }
  .card-back .brand-name { top: 345px; font-size: 42px; }

  .address {
    position: absolute;
    top: 578px;
    width: 100%;
    font-size: 17px;
    color: var(--ink-soft);
    letter-spacing: 0.5px;
  }
  .contact-row {
    position: absolute;
    top: 624px;
    width: 100%;
    font-size: 16px;
    color: var(--ink-soft);
    display: flex;
    justify-content: center;
    gap: 18px;
  }
  .contact-web { top: 655px; }
  .contact-item { display: inline-flex; align-items: center; gap: 5px; }
  .contact-item svg { fill: var(--ink-soft); }

  .website {
    position: absolute;
    top: 468px;
    width: 100%;
    font-size: 24px;
    letter-spacing: 3px;
    color: var(--ink-soft);
  }
</style>
</head>
<body>
<main class="canvas">

  <section class="card card-front" aria-label="Business card front">
    <p class="holder"><span class="holder-name">Your Name,</span> <span class="holder-position">Position</span></p>
    <div class="brand-mark" aria-hidden="true"></div>
    <h1 class="brand-name">ORA JEWELS</h1>
    <p class="address">00, Complex, Street, City, Country, 000</p>
    <div class="contact-row">
      <span class="contact-item">
        <svg width="12" height="12" viewBox="0 0 24 24" aria-hidden="true"><path d="M6.6 10.8a15 15 0 0 0 6.6 6.6l2.2-2.2a1 1 0 0 1 1-.25 11.4 11.4 0 0 0 3.6.6 1 1 0 0 1 1 1V20a1 1 0 0 1-1 1A17 17 0 0 1 3 4a1 1 0 0 1 1-1h3.5a1 1 0 0 1 1 1 11.4 11.4 0 0 0 .6 3.6 1 1 0 0 1-.25 1z"/></svg>
        +2340000000000
      </span>
      <span class="contact-item">
        <svg width="12" height="10" viewBox="0 0 24 18" aria-hidden="true"><path d="M0 0h24v18H0z M2 2l10 7 10-7" fill="var(--ink-soft)"/></svg>
        info@oramail.com
      </span>
    </div>
    <div class="contact-row contact-web">
      <span class="contact-item">
        <svg width="10" height="10" viewBox="0 0 10 10" aria-hidden="true"><circle cx="5" cy="5" r="5"/></svg>
        www.website.com
      </span>
    </div>
  </section>

  <section class="card card-back" aria-label="Business card back">
    <div class="brand-mark" aria-hidden="true"></div>
    <p class="brand-name">ORA JEWELS</p>
    <p class="website">www.website.com</p>
  </section>

</main>
</body>
</html>
```